Property Management
Bryvale Management Solutions, Inc.
Professional
Nora Dellaway, CCAM
Senior Community Manager/President
4820 Marsh Hollow Lane, Suite 300
Oxnard, CA. 93036
ndellaway@bryvalemanagementsolutions.example
www.bryvalemanagementsolutions.example

```html
<!DOCTYPE html>
<html lang="en">
<head>
<meta charset="utf-8">
<title>Bryvale Management Solutions — Stationery</title>
<link href="https://fonts.googleapis.com/css2?family=Marcellus&family=Lato:wght@400;700&display=swap" rel="stylesheet">
<style>
  :root{
    --navy:#1f4b7a;
    --slate:#6d7075;
    --paper:#ffffff;
    --ink:#3b4a5a;
    --muted:#8a93a0;
    --backdrop:#e8e3db;
  }
  *{box-sizing:border-box;margin:0;padding:0}
  html,body{width:1200px;height:446px;overflow:hidden;background:var(--backdrop)}
  body{position:relative;font-family:"Lato",sans-serif;color:var(--ink)}
  .sheet{position:absolute;background:var(--paper);box-shadow:0 2px 6px rgba(0,0,0,.18);overflow:hidden}
  .brand{display:flex;align-items:center;gap:5px}
  .brand-mark{width:8px;height:8px;background:var(--navy)}
  .brand-name{font-family:"Marcellus",serif;color:var(--navy);font-size:16px;letter-spacing:1px;line-height:1}
  .brand-sub{font-family:"Marcellus",serif;color:var(--navy);font-size:5px;letter-spacing:.5px;margin-top:2px;border-top:1px solid var(--navy);padding-top:2px;white-space:nowrap}
  .brand-sm .brand-name{font-size:13px}
  .brand-sm .brand-sub{font-size:4.2px}
  .brand-sm .brand-mark{width:6px;height:6px}
  .contact{font-size:3.8px;line-height:1.55;color:var(--ink);white-space:nowrap}
  .contact b{color:var(--navy)}
  .band{position:absolute;left:0;right:0;background:var(--navy)}

  /* Business cards */
  .card-front{left:24px;top:158px;width:115px;height:67px}
  .card-front .brand-block{position:absolute;left:10px;top:7px}
  .card-front .band{bottom:0;height:28px;padding:3px 7px;color:#fff;font-size:3.8px;line-height:1.35;white-space:nowrap}
  .card-front .band b{color:#fff}
  .card-back{left:24px;top:233px;width:115px;height:67px;display:flex;align-items:center;justify-content:center}

  /* Letterheads */
  .letterhead{top:19px;width:211px;height:401px}
  .lh-one{left:163px}
  .lh-two{left:475px}
  .letterhead .brand-block{position:absolute;left:22px;top:22px}
  .lh-one .contact{position:absolute;left:116px;top:23px}
  .lh-two .footer{position:absolute;left:0;right:0;bottom:20px}
  .lh-two .footer .band{position:static;height:6px}
  .lh-two .footer .rule{height:2px;background:var(--slate);margin-bottom:2px}
  .lh-two .footer .contact{text-align:center;margin-top:4px}

  /* Envelopes */
  .envelope-backs{position:absolute;left:845px;top:12px;width:312px;height:238px}
  .envelope-front{left:845px;top:256px;width:312px;height:90px}
  .envelope-front .brand-block{position:absolute;left:12px;top:8px}
  .envelope-front .band{bottom:8px;height:14px}
</style>
</head>
<body>

<section class="sheet card-front" aria-label="Business card front">
  <div class="brand-block brand-sm">
    <div class="brand"><span class="brand-mark"></span><span class="brand-name">BRYVALE</span></div>
    <div class="brand-sub">Management Solutions, Inc.</div>
  </div>
  <div class="band">
    <div><b>Nora Dellaway, CCAM</b></div>
    <div>Senior Community Manager/President</div>
    <div>4820 Marsh Hollow Lane, Suite 300 · Oxnard, CA. 93036</div>
    <div>ndellaway@bryvalemanagementsolutions.example</div>
  </div>
</section>

<section class="sheet card-back" aria-label="Business card back">
  <div class="brand-block brand-sm">
    <div class="brand"><span class="brand-mark"></span><span class="brand-name">BRYVALE</span></div>
    <div class="brand-sub">Management Solutions, Inc.</div>
  </div>
</section>

<section class="sheet letterhead lh-one" aria-label="Letterhead option 1">
  <div class="brand-block">
    <div class="brand"><span class="brand-mark"></span><span class="brand-name">BRYVALE</span></div>
    <div class="brand-sub">Management Solutions, Inc.</div>
  </div>
  <div class="contact">
    <div>4820 Marsh Hollow Lane, Suite 300</div>
    <div>Oxnard, CA. 93036</div>
    <div><b>Tel</b> 805.555.0142</div>
    <div><b>Fax</b> 805.555.0143</div>
    <div>www.bryvalemanagementsolutions.example</div>
  </div>
</section>

<section class="sheet letterhead lh-two" aria-label="Letterhead option 2">
  <div class="brand-block">
    <div class="brand"><span class="brand-mark"></span><span class="brand-name">BRYVALE</span></div>
    <div class="brand-sub">Management Solutions, Inc.</div>
  </div>
  <div class="footer">
    <div class="rule"></div>
    <div class="band"></div>
    <div class="contact">4820 Marsh Hollow Lane, Suite 300 · Oxnard, CA. 93036 · www.bryvalemanagementsolutions.example</div>
  </div>
</section>

<svg class="envelope-backs" viewBox="0 0 312 238" aria-label="Envelope backs">
  <g>
    <rect x="0" y="0" width="312" height="80" fill="#fff"/>
    <path d="M0 0 H312 V20 L180 62 Q156 70 132 62 L0 20 Z" fill="var(--navy)"/>
  </g>
  <g transform="translate(0,82)">
    <rect x="0" y="0" width="312" height="76" fill="#fff"/>
    <path d="M0 0 H312 V18 L180 58 Q156 66 132 58 L0 18 Z" fill="var(--slate)"/>
  </g>
  <g transform="translate(0,160)">
    <rect x="0" y="0" width="312" height="76" fill="#fff"/>
    <path d="M0 0 H312 V18 L180 58 Q156 66 132 58 L0 18 Z" fill="#f4f4f4" stroke="#d6d6d6" stroke-width="0.6"/>
  </g>
</svg>

<section class="sheet envelope-front" aria-label="Envelope front">
  <div class="brand-block brand-sm">
    <div class="brand"><span class="brand-mark"></span><span class="brand-name">BRYVALE</span></div>
    <div class="brand-sub">Management Solutions, Inc.</div>
  </div>
  <div class="band"></div>
</section>

</body>
</html>
```